Fitness Clothing Apparel Business Card

This project is linked to Fitness Clothing Apparel, KESTRO, Looking for AWESOME Logo Design!!!.

Our company needs a Business Card Design. Please refer to our original project in the link above.

Hi, I'm looking for a professional logo design which will help brand my clothing and nutrition supplement company. The winner of this contest may be hired again in the future to help design some flyers, banners, graphics, etc.

A little background about the company...
KESTRO Fitness is a new fitness clothing and nutrition company based in Southern California... near the mecca of bodybuilding, Harlow Cove! Our company is based around the culture of fitness and bodybuilding. We design clothing that are functional yet appealing for an athletic individual.

What I would like to see on business card...
The card has communicate our brand values. It needs to have attitude yet professionally done. Our brand colors are black, red, and white.

Target Market(s)

Fitness and bodybuilding enthusiasts

Industry/Entity Type

Nutrition

Font styles to use
Serif
Sans Serif
Decorative
Script

Colors

Designer to choose colors to be used in the design.

Requirements
Must have
• our company logo
Nice to have
• red and black, an abstract design of a bull
Should not have
• I'm open to all ideas, appearance is important

```html
<!DOCTYPE html>
<html lang="en">
<head>
<meta charset="utf-8">
<title>KESTRO Business Card</title>
<link href="https://fonts.googleapis.com/css2?family=Jost:wght@300&family=Open+Sans:wght@400&display=swap" rel="stylesheet">
<style>
  :root {
    --backdrop: #2b2623;
    --card: #141414;
    --card-edge: #1e1e1e;
    --ink: #f2f2f2;
    --ink-soft: #cfcfcf;
    --emboss: #3a3a3a;
  }
  * { margin: 0; padding: 0; box-sizing: border-box; }
  html, body { width: 1200px; height: 720px; overflow: hidden; }
  body {
    background: var(--backdrop);
    position: relative;
    font-family: "Open Sans", Arial, sans-serif;
  }
  .card {
    position: absolute;
    top: 210px;
    width: 525px;
    height: 300px;
    background: var(--card);
    border: 1px solid var(--card-edge);
    box-shadow: 0 18px 40px rgba(0,0,0,.45);
  }
  .card--back { left: 45px; }
  .card--front { left: 630px; }

  .back-mark {
    position: absolute;
    left: 50%;
    top: 50%;
    transform: translate(-50%, -50%);
    font-family: "Jost", Arial, sans-serif;
    font-weight: 300;
    font-size: 64px;
    letter-spacing: 18px;
    color: var(--emboss);
  }

  .brand {
    position: absolute;
    left: 34px;
    top: 118px;
    display: flex;
    align-items: center;
    gap: 14px;
  }
  .brand-dot {
    width: 14px; height: 14px;
    border-radius: 50%;
    background: var(--ink);
  }
  .brand-name {
    font-family: "Jost", Arial, sans-serif;
    font-weight: 300;
    font-size: 40px;
    letter-spacing: 12px;
    color: var(--ink);
  }

  .contact {
    position: absolute;
    left: 320px;
    top: 100px;
    color: var(--ink);
  }
  .person-name { font-size: 15px; }
  .person-role { font-size: 11px; color: var(--ink-soft); margin-top: 2px; }
  .contact-list { list-style: none; margin-top: 20px; }
  .contact-list li {
    display: flex;
    align-items: center;
    gap: 8px;
    font-size: 12px;
    line-height: 20px;
  }
  .contact-list svg { width: 10px; height: 10px; fill: var(--ink); flex: none; }
</style>
</head>
<body>
  <div class="card card--back">
    <span class="back-mark">KESTRO</span>
  </div>

  <div class="card card--front">
    <div class="brand">
      <span class="brand-dot"></span>
      <span class="brand-name">KESTRO</span>
    </div>

    <div class="contact">
      <p class="person-name">Dane Holloway</p>
      <p class="person-role">Founder / CEO</p>
      <ul class="contact-list">
        <li>
          <svg viewBox="0 0 10 10"><path d="M2 0.5 L3.6 2.6 L2.8 3.6 Q4 6 6.4 7.2 L7.4 6.4 L9.5 8 L8.4 9.5 Q4 9 0.5 1.6 Z"/></svg>
          +61 3 9480 5512
        </li>
        <li>
          <svg viewBox="0 0 10 10"><path d="M0 2 H10 V8.5 H0 Z M0.6 2.6 L5 5.6 L9.4 2.6" stroke="#141414" stroke-width="0.8"/></svg>
          dane@kestro.com
        </li>
        <li>
          <svg viewBox="0 0 10 10"><circle cx="5" cy="5" r="4.6"/><path d="M0.5 5 H9.5 M5 0.5 Q2.5 5 5 9.5 M5 0.5 Q7.5 5 5 9.5" stroke="#141414" stroke-width="0.7" fill="none"/></svg>
          www.kestro.com
        </li>
      </ul>
    </div>
  </div>
</body>
</html>
```